Brivolt Flyer for Logistics Fair

We are a leading Shelving & Warehouse Systems Specialist supplying consultancy, design and end to end project implementation for Retail and Warehouses. We seek a brochure that is simple yet communicates our products and services in a handout pamphlet.

Target Market(s)

Warehouse and Factory buyers looking for racks needed in their facility

Industry/Entity Type

Retail

Font styles to use
Serif
Sans Serif

Colors
000000

Requirements
Must have
• Company name and logo ( Brivolt)
• Pictures of Rack & Conveying systems
• Products we do
• Services we provide
• Focus on " Soecialist in Retail & Warehouses Solutions "
Nice to have
• Easy to understand layout and flow
• Modern-day and trendy feel
Should not have
• Not be cluttered
• Not too wordy
• Pls do not use pic of factory or equipments .....

```html
<!DOCTYPE html>
<html lang="en">
<head>
<meta charset="utf-8">
<title>Brivolt Flyer</title>
<link href="https://fonts.googleapis.com/css2?family=Oswald:wght@400;500&family=Open+Sans:ital,wght@0,400;0,600;1,400;1,700&display=swap" rel="stylesheet">
<style>
:root{
  --ink:#231f20;
  --row-alt:#38363a;
  --yellow:#ffe500;
  --yellow-dark:#c9a400;
  --panel:#f1f1f1;
  --silver-light:#fafafa;
  --silver-mid:#d2d2d2;
  --white:#ffffff;
  --text:#2a2a2a;
}
*{margin:0;padding:0;box-sizing:border-box}
html,body{width:880px;height:1200px;overflow:hidden;background:var(--white)}
.flyer{position:relative;width:880px;height:1200px;overflow:hidden;font-family:"Open Sans",Arial,sans-serif;color:var(--text);
  background:linear-gradient(135deg,var(--silver-light) 0%,var(--silver-mid) 30%,var(--white) 55%,var(--silver-mid) 80%,var(--silver-light) 100%)}
.hero-art{position:absolute;left:0;top:0;width:880px;height:624px}
.contact-email{position:absolute;left:40px;top:84px;display:flex;align-items:center;gap:10px;font-style:italic;font-size:15px;color:var(--ink)}
.brand-bar{position:absolute;left:0;top:118px;width:386px;height:100px;background:linear-gradient(180deg,#4a4a4a,#2a2a2a);
  border:3px solid #c8c8c8;border-left:none;display:flex;flex-direction:column;justify-content:center;padding-left:40px;gap:2px}
.brand-row{display:flex;align-items:center;gap:14px}
.brand-mark{width:24px;height:24px;border-radius:50%;background:var(--white)}
.brand-name{font-size:44px;line-height:50px;font-weight:400;color:var(--white);letter-spacing:1px}
.brand-focus{font-family:"Oswald",Arial,sans-serif;font-weight:400;font-size:14px;letter-spacing:.8px;color:var(--yellow);text-transform:uppercase}
.services-head,.what-head{position:absolute;font-family:"Oswald",Arial,sans-serif;font-weight:500;color:var(--white);font-size:34px;letter-spacing:-.5px}
.services-head{left:0;top:624px;width:324px;height:60px;background:var(--ink);clip-path:polygon(0 0,264px 0,324px 60px,0 60px);padding:6px 0 0 44px}
.what-head{left:530px;top:625px;width:284px;height:60px;background:var(--ink);clip-path:polygon(0 0,232px 0,284px 60px,0 60px);padding:8px 0 0 25px}
.services-panel{position:absolute;left:0;top:684px;width:530px;height:412px;background:var(--panel);
  display:flex;flex-direction:column;justify-content:center;padding:0 30px 0 46px}
.service{display:flex;gap:34px;font-size:15.6px;line-height:25px;padding:13px 0}
.service + .service{border-top:1px dotted #9a9a9a}
.service svg{flex:none;margin-top:3px}
.service p{width:386px}
.service em{font-style:italic;font-weight:700}
.what-panel{position:absolute;left:530px;top:684px;width:350px;height:412px;background:var(--ink)}
.offer{position:absolute;left:586px;width:294px;height:67px;display:flex;align-items:center;padding-left:24px;
  font-size:28px;color:var(--white);border-bottom:2px dotted #555}
.offer.alt{background:var(--row-alt)}
.offer-icon{position:absolute;left:516px;width:68px;height:67px;display:flex;align-items:center;justify-content:center}
.offer-icon.yellow{background:var(--yellow)}
.offer-icon.grey{background:#e6e6e6}
.offer-icon::after{content:"";position:absolute;left:0;bottom:-7px;border-top:7px solid var(--yellow-dark);border-left:12px solid transparent}
.offer-icon.grey::after{border-top-color:#a0a0a0}
.footer{position:absolute;left:0;top:1100px;width:880px;height:100px;
  background:linear-gradient(180deg,#bdbdbd 0%,var(--white) 40%,#d6d6d6 100%);display:flex;align-items:center}
.phone{display:flex;align-items:center;gap:5px;font-family:"Oswald",Arial,sans-serif;font-weight:400;font-size:24px;color:var(--ink);letter-spacing:-.5px}
.phone.fax{margin-left:38px}
.phone.tel{margin-left:28px}
.footer-rule{width:1px;height:58px;background:#999;margin-left:20px}
.address{display:flex;align-items:center;gap:14px;margin-left:16px;font-size:10.4px;line-height:16px;color:var(--ink)}
</style>
</head>
<body>
<div class="flyer">
  <svg class="hero-art" viewBox="0 0 880 624" xmlns="http://www.w3.org/2000/svg">
    <defs>
      <linearGradient id="swoosh" x1="0" y1="0" x2="1" y2="1">
        <stop offset="0" stop-color="#ffffff"/><stop offset=".5" stop-color="#a8a8a8"/><stop offset="1" stop-color="#f4f4f4"/>
      </linearGradient>
      <linearGradient id="warehouse" x1="0" y1="0" x2="0" y2="1">
        <stop offset="0" stop-color="#5f6a5c"/><stop offset=".4" stop-color="#8f8a7c"/><stop offset=".7" stop-color="#c9b9a0"/><stop offset="1" stop-color="#5a4e45"/>
      </linearGradient>
    </defs>
    <path d="M40 560 C120 280 420 40 760 40 C860 40 900 120 880 160 L880 0 L0 0 L0 560 Z" fill="#e4e4e4" opacity=".6"/>
    <path d="M60 600 C20 360 320 40 720 30 C900 25 880 200 820 320 C870 180 820 60 700 60 C360 70 80 330 60 600 Z" fill="url(#swoosh)"/>
    <path d="M430 610 C700 600 860 470 880 360 L880 420 C840 520 680 620 430 610 Z" fill="url(#swoosh)"/>
    <ellipse cx="470" cy="306" rx="330" ry="266" transform="rotate(-14 470 306)" fill="url(#warehouse)" role="img" aria-label="Photo of a tall warehouse pallet racking system with blue uprights and orange beams stacked with boxed goods"/>
    <ellipse cx="470" cy="306" rx="330" ry="266" transform="rotate(-14 470 306)" fill="none" stroke="#ffffff" stroke-width="6"/>
  </svg>

  <div class="contact-email">
    <svg width="20" height="14" viewBox="0 0 20 14"><rect x="1" y="1" width="18" height="12" fill="none" stroke="#231f20" stroke-width="2"/><path d="M1 1 L10 8 L19 1" fill="none" stroke="#231f20" stroke-width="2"/></svg>
    sales@brivolt-systems.com
  </div>

  <div class="brand-bar">
    <div class="brand-row"><span class="brand-mark"></span><span class="brand-name">BRIVOLT</span></div>
    <div class="brand-focus">Specialist in Retail &amp; Warehouses Solutions</div>
  </div>

  <div class="services-head">OUR SERVICES</div>
  <div class="what-head">WHAT WE DO</div>

  <div class="services-panel">
    <div class="service">
      <svg width="26" height="24" viewBox="0 0 26 24"><rect x="2" y="5" width="18" height="17" fill="none" stroke="#231f20" stroke-width="2" stroke-dasharray="3 2"/><path d="M6 12 L11 17 L24 2" fill="none" stroke="#231f20" stroke-width="3"/></svg>
      <p>Complete metal shelving systems with a wide range of accessories for <em>Hypermarkets, Supermarkets</em> and <em>Convenience stores.</em></p>
    </div>
    <div class="service">
      <svg width="26" height="24" viewBox="0 0 26 24"><rect x="2" y="5" width="18" height="17" fill="none" stroke="#231f20" stroke-width="2" stroke-dasharray="3 2"/><path d="M6 12 L11 17 L24 2" fill="none" stroke="#231f20" stroke-width="3"/></svg>
      <p>Racking &amp; conveying systems suitable for <em>cash &amp; carry outlets</em>, <em>D.I.Y retailers</em> and <em>small to medium warehouses.</em></p>
    </div>
    <div class="service">
      <svg width="26" height="24" viewBox="0 0 26 24"><rect x="2" y="5" width="18" height="17" fill="none" stroke="#231f20" stroke-width="2" stroke-dasharray="3 2"/><path d="M6 12 L11 17 L24 2" fill="none" stroke="#231f20" stroke-width="3"/></svg>
      <p>Cash counters <em>customized</em> to retailers requirement.</p>
    </div>
    <div class="service">
      <svg width="26" height="24" viewBox="0 0 26 24"><rect x="2" y="5" width="18" height="17" fill="none" stroke="#231f20" stroke-width="2" stroke-dasharray="3 2"/><path d="M6 12 L11 17 L24 2" fill="none" stroke="#231f20" stroke-width="3"/></svg>
      <p>A wide range of <em>shop fitting systems</em> to <em>cater</em> to department stores and <em>specialized retail.</em></p>
    </div>
  </div>

  <div class="what-panel"></div>

  <div class="offer-icon yellow" style="top:705px">
    <svg width="28" height="22" viewBox="0 0 28 22"><path d="M1 2 H6 L9 14 H23 L26 5 H7" fill="none" stroke="#231f20" stroke-width="2.5"/><circle cx="11" cy="19" r="2" fill="#231f20"/><circle cx="21" cy="19" r="2" fill="#231f20"/></svg>
  </div>
  <div class="offer" style="top:705px">Supermarket</div>

  <div class="offer-icon grey" style="top:780px">
    <svg width="24" height="24" viewBox="0 0 24 24"><path d="M3 8 H21 L19 23 H5 Z" fill="#231f20"/><path d="M8 10 V5 a4 4 0 0 1 8 0 V10" fill="none" stroke="#231f20" stroke-width="2"/></svg>
  </div>
  <div class="offer alt" style="top:780px">Hypermarket</div>

  <div class="offer-icon yellow" style="top:855px">
    <svg width="26" height="26" viewBox="0 0 26 26"><path d="M3 6 L23 3 M3 13 L23 11 M3 21 L23 19 M5 4 V24 M13 4 V22 M21 3 V22" fill="none" stroke="#231f20" stroke-width="2.5"/></svg>
  </div>
  <div class="offer" style="top:855px">Racking System</div>

  <div class="offer-icon grey" style="top:930px">
    <svg width="28" height="18" viewBox="0 0 28 18"><path d="M2 2 V16 M6 2 L14 16 M14 9 a5 5 0 1 1 10 0 a5 5 0 1 1 -10 0" fill="none" stroke="#231f20" stroke-width="2.5"/></svg>
  </div>
  <div class="offer alt" style="top:930px">Shop Fitting</div>

  <div class="offer-icon yellow" style="top:1005px">
    <svg width="26" height="28" viewBox="0 0 26 28"><rect x="6" y="2" width="12" height="7" fill="none" stroke="#231f20" stroke-width="2"/><rect x="3" y="11" width="20" height="10" fill="none" stroke="#231f20" stroke-width="2"/><path d="M7 15 H9 M12 15 H14 M17 15 H19" stroke="#231f20" stroke-width="2"/><rect x="1" y="22" width="24" height="5" fill="#231f20"/></svg>
  </div>
  <div class="offer" style="top:1005px">Cash Counter</div>

  <div class="footer">
    <div class="phone fax">
      <svg width="22" height="22" viewBox="0 0 22 22"><rect x="1" y="7" width="20" height="14" rx="2" fill="#231f20"/><rect x="5" y="1" width="12" height="7" fill="none" stroke="#231f20" stroke-width="2"/><path d="M10 11 H18 M10 14 H18 M10 17 H18" stroke="#fff" stroke-width="1.5"/></svg>
      +661-5550123-4
    </div>
    <div class="phone tel">
      <svg width="20" height="20" viewBox="0 0 20 20"><rect x="0" y="0" width="20" height="20" rx="4" fill="#231f20"/><path d="M6 4 L8 7 L7 9 Q9 12 11 13 L13 12 L16 14 L14 16 Q8 16 4 8 Z" fill="#fff"/></svg>
      +661-5550456-78
    </div>
    <div class="footer-rule"></div>
    <div class="address">
      <svg width="16" height="22" viewBox="0 0 16 22"><path d="M8 1 a7 7 0 0 1 7 7 c0 5 -7 13 -7 13 S1 13 1 8 a7 7 0 0 1 7 -7 Z" fill="#231f20"/><circle cx="8" cy="8" r="3" fill="#fff"/></svg>
      <p>Harbour Point Tower, 21st Floor, 48/12-14 Soi Riverside 7, Lakeview Road,<br>North Central District, Eastgate City 20450 Thailand</p>
    </div>
  </div>
</div>
</body>
</html>
```